Geschäftspapiere für Kanzlei
Zielgruppe
Forschungsinstitute und Großunternehmen die eigene Entwicklungsabteilungen haben und Erfindungen patentieren lassen.
Aufgabenstellung
Möglicherweise ergibt eine Weiterentwiklung unseres logos Sinn? Denkbar wäre für uns aber auch auf das Logo ganz zu verzichten.
Es sollte nicht mehr als eine Farbe (Blauton) verwendet werden. Wir wollen schlicht, klassisch und seriös auftreten.

```html
<!DOCTYPE html>
<html lang="de">
<head>
<meta charset="utf-8">
<title>Briefbogen – Patentanwaltskanzlei Dr. Tamar Velidze</title>
<link rel="stylesheet" href="https://fonts.googleapis.com/css2?family=Libre+Franklin:wght@400;600&display=swap">
<style>
  :root {
    --backdrop: #1d3149;
    --paper: #f4f4f4;
    --brand-blue: #1f3466;
    --ink: #2a2a2a;
  }
  * { box-sizing: border-box; margin: 0; padding: 0; }
  html, body {
    width: 1200px; height: 860px; overflow: hidden;
    background: var(--backdrop);
    font-family: "Libre Franklin", Arial, sans-serif;
  }
  .letterhead {
    position: absolute;
    left: 324px; top: 40px;
    width: 552px; height: 780px;
    background: var(--paper);
    box-shadow: 0 6px 18px rgba(0,0,0,0.35);
    color: var(--ink);
  }
  .brand {
    position: absolute; left: 48px; top: 46px;
    display: flex; align-items: center; gap: 10px;
  }
  .brand-square {
    width: 14px; height: 14px; background: var(--brand-blue);
  }
  .brand-name {
    font-weight: 600; font-size: 15px; letter-spacing: 0.12em;
    text-transform: uppercase; color: var(--brand-blue);
  }
  .brand-tagline {
    position: absolute; left: 72px; top: 68px;
    font-size: 8px; letter-spacing: 0.28em; text-transform: uppercase;
    color: var(--brand-blue);
  }
  .sender-line {
    position: absolute; left: 48px; top: 150px;
    font-size: 7.5px; letter-spacing: 0.02em;
  }
  .contact-block {
    position: absolute; left: 392px; top: 172px;
    font-size: 6.5px; line-height: 1.45;
  }
  .contact-block p + p { margin-top: 7px; }
  .footer {
    position: absolute; left: 0; right: 0; bottom: 30px;
    text-align: center; font-size: 6.5px; line-height: 1.5;
  }
</style>
</head>
<body>
  <main class="letterhead">
    <div class="brand">
      <span class="brand-square"></span>
      <span class="brand-name">Dr. Tamar Velidze</span>
    </div>
    <div class="brand-tagline">Patentanwaltskanzlei</div>

    <p class="sender-line">Kanzlei Dr. Velidze • Lindenhofstrasse 42 • 80339 München</p>

    <div class="contact-block">
      <p>Dr. rer. nat. Tamar Velidze, PhD<br>Patentanwalt<br>European Patent Attorney<br>European Design- und Trademark Attorney</p>
      <p>Lindenhofstrasse 42<br>80339 München</p>
      <p>Tel.: + 49 89 430 118 260<br>Fax: + 49 89 430 118 29<br>Email: kontakt@velidze-ip.de</p>
    </div>

    <footer class="footer">
      Patentanwaltskanzlei Dr. Velidze, Steuernummer.: 143/208/51937, www.velidze-ip.de<br>
      Nordmark Bank, Konto: 4300918276, IBAN: DE12700100804300918276, BLZ: 70010080, BIC: NORMDEM1XXX
    </footer>
  </main>
</body>
</html>
```